Business Card Design

I am an insurance agent and do most of my work from home. I want to change the attached business card to reflect my home address, cell phone number and email address. Perhaps I want my business address and business phone and fax on the back. I like the card attached. But it has all houses. I would like a house, car, motorcycle, boat, business and life insurance logos instead of just houses. My work address is KMT Insurance Agency; 5816 Wexley Parkway, Suite 410; Falls Church, Virginia 22046-3917. My home address is 931 Millbrook Lane; Woodbridge, Virginia 22193-2684. I want it to have my name and the company name and my address. I like everything spelled out. I do not like abbreviations. I want a card that stands out. Maybe even a little bit silly like the one attached but still to be professional.
Updates

I want my home address on the front and work address on the back.

Home: 931 Millbrook Lane; Woodbridge, Virginia 22193-2684

Work: 5816 Wexley Parkway, Suite 410; Falls Church, Virginia 22046-3917
                                                                

I re-read what I wrote and tried to make it clearer; so there are some minor changes.

The PDF business card I uploaded did not appear to be readable.  I scanned it in as a JPG and uploaded it.  It is not as clear but is readable.  I just want you to see what I currently have and sort of like.

Target Market(s)

Insurance Customers. Mostly by mail or email

Industry/Entity Type

Life Insurance

Contact Information for Business Card

KMT Insurance Agency Dennis R Whitcombe
931 Millbrook Lane; Woodbridge, Virginia 22193-2684
Cell phone: (703) 555-4162 DWHITCOMBE@MAILNEST.EXAMPLE

Colors

Designer to choose colors to be used in the design.

Requirements
Must have
• On the front I want my home information and on the back perhaps my office information. I go to the office once a week or less. So I want to be contacted by email or my cell. I want them to mail stuff to my house. I don't want them to contact my office unless they cannot reach me. I have my email address in all capitals because it starts with an "L" and that could be a 1, I, or L. I have another email address: whitcombe@postvale.example and perhaps I should use that one or both.
Nice to have
• Auto, Boat, Business, Commercial, Home, Life & Health, Motorcycle.
It would be nice to say this across the card if not too long and to have some of these logos displayed, per the attached card.
Should not have
• I like things spelled out, such as Street rather than ST or Virginia rather than VA. But Cell Phone or Cell as you think best.

```html
<!DOCTYPE html>
<html lang="en">
<head>
<meta charset="utf-8">
<title>Dennis R Whitcombe – Business Cards</title>
<link rel="stylesheet" href="https://fonts.googleapis.com/css2?family=Marcellus+SC&family=Arimo:wght@400&display=swap">
<style>
  :root {
    --backdrop: #e9dcc4;
    --card: #ffffff;
    --orange: #e0922a;
    --orange-fade: #f6e2c8;
    --ink: #111111;
    --mark-tone: #dfe6e2;
    --mark-edge: #1f3328;
  }
  * { box-sizing: border-box; margin: 0; padding: 0; }
  html, body {
    width: 1200px;
    height: 900px;
    overflow: hidden;
    background: var(--backdrop);
  }
  .canvas {
    position: relative;
    width: 1200px;
    height: 900px;
  }
  .card {
    position: absolute;
    width: 560px;
    height: 310px;
    background: var(--card);
    box-shadow: 0 6px 18px rgba(0,0,0,0.18);
    overflow: hidden;
  }
  .card--front { left: 80px; top: 90px; }
  .card--back  { left: 560px; top: 500px; }

  .card__header {
    position: absolute;
    left: 0; top: 24px;
    width: 100%;
    height: 96px;
    background: linear-gradient(90deg, var(--orange) 0%, var(--orange) 8%, var(--orange-fade) 62%, var(--card) 100%);
    padding: 12px 26px 0;
  }
  .card__name {
    font-family: "Marcellus SC", serif;
    font-size: 38px;
    font-weight: 400;
    line-height: 1;
    color: var(--ink);
    letter-spacing: 0.5px;
  }
  .card__role {
    font-family: "Arimo", sans-serif;
    font-size: 21px;
    color: var(--ink);
    margin-top: 10px;
    letter-spacing: 0.4px;
  }
  .card__contact {
    position: absolute;
    left: 26px;
    top: 158px;
    font-family: "Arimo", sans-serif;
    font-size: 16px;
    line-height: 25px;
    color: var(--ink);
  }
  .card--back .card__contact { top: 196px; }
  .card--back .card__contact .card__line--small { font-size: 14px; }
  .card__mark {
    position: absolute;
    right: 40px;
    top: 136px;
    width: 170px;
    height: 132px;
    background: var(--mark-tone);
    border-bottom: 3px solid var(--mark-edge);
  }
  .card__footer {
    position: absolute;
    left: 0; bottom: 0;
    width: 100%;
    height: 40px;
    background: var(--orange);
  }
</style>
</head>
<body>
<main class="canvas">

  <section class="card card--front" aria-label="Business card front">
    <header class="card__header">
      <h1 class="card__name">Dennis R Whitcombe</h1>
      <p class="card__role">Insurance Agent</p>
    </header>
    <div class="card__contact">
      <p class="card__line">Cell phone: (703) 555-4162</p>
      <p class="card__line">DWHITCOMBE@MAILNEST.EXAMPLE</p>
      <p class="card__line">Home: 931 Millbrook Lane;</p>
      <p class="card__line">Woodbridge, Virginia 22193-2684</p>
    </div>
    <div class="card__mark" role="img" aria-label="Line drawing of a house, agency emblem"></div>
    <div class="card__footer"></div>
  </section>

  <section class="card card--back" aria-label="Business card back">
    <header class="card__header">
      <h2 class="card__name">Dennis R Whitcombe</h2>
      <p class="card__role">KMT Insurance Agency</p>
    </header>
    <div class="card__contact">
      <p class="card__line">Tel phone: (703) 555-0193</p>
      <p class="card__line card__line--small">Work: 5816 Wexley Parkway, Suite</p>
      <p class="card__line card__line--small">410; Falls Church, Virginia 22046-3917</p>
    </div>
    <div class="card__mark" role="img" aria-label="Line drawing of a house, agency emblem"></div>
    <div class="card__footer"></div>
  </section>

</main>
</body>
</html>
```